Gourmet food company looking for a dazzling label for their premuim vinagrette dressings

Need a food label that will dazzle our customer and prove what a premium product we have. We make high end gourmet dressing for vegetables, fruit, meat, poultry and fish.

Our label will fit on a 250 mil Tolvenna Square bottle. Labels should be a 4x5 or even 5x5 depending on the design. Nutritionals, bar codes and company blurb will be supplied later. We really want to test you all's talent on this one and are very excited to see your renderings!

Our dressings are Champagne Pear Vinaigrette, White Balsmic Vinaigrette, Mojito Lime Vinaigrette, Creamy-Avacado Lime Vinaigrette, and Asian Sesame Vinaigrette. I hope these names will help you envision our product and kinda what we are looking for.

Thank you all so far for your renderings.I really don't want pictures if that helps. Our logo can be smaller and/or the name of the product bigger. Perhaps we can even redesign Lumora and remove the leaf as I don't really care for what I see yet.So good luck and thanks Added Friday, August 19, 2016

I am still looking for that clean - elegant design for our product as our product is just that. If you look on the internet at vinegars and oils you will see many designs that are simple yet elegant. Creative lettering, bordering, color (can be black and white) and size will help accomplish this. So I invite you to use all your creativity and help me find just what we need.Many thanks Added Tuesday, August 23, 2016

Project Deadline Extended Reason: So many great designs coming in that I wanted a few extra days to tweek!Great job all Added Friday, August 26, 2016

Project Deadline Extended Reason: Very good designs thus far. We just need a few more days.Thanks Added Wednesday, August 31, 2016

Target Market(s)

High end grocery and specialty stores.

Our side panel on the label will say "At Lumora we're fanatics for great flavors and are passionate about finding the best ingredients. From simple to elegant our products are "simply lumora".

Industry/Entity Type

It Company

Font styles to use
Serif
Decorative
Script

Requirements
Must have
• A label that will draw the consumer to pick it up! Need something bold and elegant...
Nice to have
• Again, I really would like to have a label that pops. Since the bottle front is only about 2inches in width it will need some creativity. Would like something very simple and elegant.
• If the designer does not like the logo, please feel free to design without it!
Should not have
• Dark dark colors. We are selling dressing and we don't want any colors that may distort the contents.
• No stock photos for the front. I don't want our dressing to look like the others on the self. Brackwell Pantry just uses lettering and a their packaging is eye catching

```html
<!DOCTYPE html>
<html lang="en">
<head>
<meta charset="utf-8">
<title>Lumora – Champagne Pear Vinaigrette Label</title>
<link rel="stylesheet" href="https://fonts.googleapis.com/css2?family=Bitter:ital,wght@0,500;0,600;1,700&family=Playball&display=swap">
<style>
  :root {
    --cream: #f9f3e8;
    --band: #d9dcdb;
    --ink: #111111;
    --brand-brown: #3a2418;
    --frame: #1c1c1c;
    --panel-white: #ffffff;
    --panel-grey: #8f8f8f;
    --flourish: #3a3a3a;
    --faint-flourish: #c3c6c5;
    --shadow: rgba(90, 75, 70, 0.35);
  }
  * { margin: 0; padding: 0; box-sizing: border-box; }
  html, body { width: 1200px; height: 960px; overflow: hidden; background: var(--cream); }
  .label {
    position: relative;
    width: 1200px;
    height: 960px;
    background: var(--cream);
    overflow: hidden;
    color: var(--ink);
  }
  .frame { position: absolute; inset: 0; }
  .band {
    position: absolute;
    left: 0; top: 347px;
    width: 1200px; height: 344px;
    background: var(--band);
    box-shadow: 0 22px 30px -6px var(--shadow);
  }
  .band-flourish {
    position: absolute;
    left: 40px; top: 352px;
    width: 190px; height: 338px;
    background: linear-gradient(180deg, var(--faint-flourish), rgba(195,198,197,0.3));
    opacity: 0.5;
    border-radius: 40% 60% 30% 50%;
  }
  .headline {
    position: absolute;
    left: 30px; top: 170px;
    width: 360px;
    font-family: "Playball", cursive;
    font-weight: 400;
    font-size: 40px;
    line-height: 54px;
    color: var(--ink);
  }
  .blurb {
    position: absolute;
    left: 48px; top: 404px;
    width: 305px;
    font-family: "Bitter", serif;
    font-weight: 600;
    font-size: 23px;
    line-height: 33px;
    letter-spacing: 0.6px;
    color: var(--ink);
    text-shadow: 4px 8px 14px rgba(0,0,0,0.18);
  }
  .ornament {
    position: absolute;
    background: var(--flourish);
    opacity: 0.55;
  }
  .ornament--top { left: 555px; top: 62px; width: 90px; height: 62px; border-radius: 50% 50% 30% 30%; }
  .ornament--bottom { left: 555px; top: 272px; width: 90px; height: 62px; border-radius: 30% 30% 50% 50%; }
  .ornament--title { left: 500px; top: 605px; width: 180px; height: 54px; border-radius: 50%; }
  .brand {
    position: absolute;
    left: 395px; top: 158px;
    width: 410px;
    text-align: center;
    font-family: "Bitter", serif;
    font-weight: 500;
    font-size: 50px;
    color: var(--brand-brown);
  }
  .product-name {
    position: absolute;
    left: 380px; top: 372px;
    width: 420px;
    text-align: center;
    font-family: "Playball", cursive;
    font-weight: 400;
    color: var(--ink);
    white-space: nowrap;
  }
  .product-name .line-1 { display: block; font-size: 60px; line-height: 82px; }
  .product-name .line-2 { display: block; font-size: 90px; line-height: 110px; }
  .panel-main {
    position: absolute;
    left: 857px; top: 205px;
    width: 285px; height: 510px;
    background: var(--panel-white);
    padding: 50px 27px 37px 23px;
  }
  .panel-main .panel-fill { width: 235px; height: 423px; background: var(--panel-grey); }
  .panel-small {
    position: absolute;
    left: 891px; top: 728px;
    width: 217px; height: 120px;
    background: var(--panel-white);
    padding: 10px 16px 6px 15px;
  }
  .panel-small .panel-fill { width: 186px; height: 104px; background: var(--panel-grey); }
  .net-weight {
    position: absolute;
    left: 375px; top: 838px;
    width: 400px;
    text-align: center;
    font-family: "Bitter", serif;
    font-style: italic;
    font-weight: 700;
    font-size: 24px;
    color: var(--ink);
    text-shadow: 0 14px 12px rgba(0,0,0,0.12);
  }
</style>
</head>
<body>
<main class="label">
  <svg class="frame" width="1200" height="960" viewBox="0 0 1200 960" aria-hidden="true">
    <path d="M0 117 H388 C386 88 394 62 436 54 C466 22 521 12 596 12 C671 12 726 22 756 54 C798 62 806 88 804 117 H1200"
          fill="none" stroke="var(--frame)" stroke-width="3"/>
    <line x1="0" y1="117" x2="0" y2="952" stroke="var(--frame)" stroke-width="3"/>
    <line x1="0" y1="952" x2="1200" y2="952" stroke="var(--frame)" stroke-width="3"/>
    <line x1="388" y1="130" x2="790" y2="130" stroke="var(--frame)" stroke-width="3"/>
    <line x1="388" y1="265" x2="790" y2="265" stroke="var(--frame)" stroke-width="3"/>
  </svg>

  <div class="band"></div>
  <div class="band-flourish" role="img" aria-label="Faint swirling flourish decoration"></div>

  <div class="ornament ornament--top" role="img" aria-label="Scrolled flourish ornament above the brand name"></div>
  <p class="brand">Lumora</p>
  <div class="ornament ornament--bottom" role="img" aria-label="Scrolled flourish ornament below the brand name"></div>

  <p class="headline">At Lumora, we’re fanatics for great flavours…</p>

  <p class="blurb">… and are passionate about finding the best ingredients. From simple to elegant our products are “simply lumora”.</p>

  <h1 class="product-name">
    <span class="line-1">Champagne Pear</span>
    <span class="line-2">Vinaigrette</span>
  </h1>
  <div class="ornament ornament--title" role="img" aria-label="Calligraphic swash flourish under the product name"></div>

  <div class="panel-main"><div class="panel-fill"></div></div>
  <div class="panel-small"><div class="panel-fill"></div></div>

  <p class="net-weight">net weight: 250 fl ml</p>
</main>
</body>
</html>
```